Business Card Design Project

Small privately owned salon.

Industry/Entity Type

Business

Contact Information for Business Card

Hair salon.i would like my logo to be my name , Rosalind Marie. Address and phone can go on the front or back. The back will be where I write their appt.
address-527 Willowbend lane York, Pa. 17402
Phone- 717-464-3082

```html
<!DOCTYPE html>
<html lang="en">
<head>
<meta charset="utf-8">
<title>Rosalind Marie Hair Salon – Business Card</title>
<link rel="stylesheet" href="https://fonts.googleapis.com/css2?family=Tinos:ital,wght@0,400;0,700;1,400&family=Montserrat:ital,wght@0,400;0,600;1,300&display=swap">
<style>
  :root {
    --stage: #ece3d3;
    --card: #000000;
    --ink: #ffffff;
    --gold: #c99a4e;
    --gold-soft: #a7834a;
    --rule: #d8d8d8;
  }
  * { box-sizing: border-box; margin: 0; padding: 0; }
  html, body {
    width: 1012px;
    height: 1200px;
    overflow: hidden;
    background: var(--stage);
  }
  .card {
    position: absolute;
    left: 139px;
    width: 727px;
    height: 419px;
    background: var(--card);
    color: var(--ink);
    overflow: hidden;
  }
  .card--front { top: 115px; }
  .card--back { top: 650px; }

  /* Front */
  .brand {
    position: absolute;
    left: 0;
    right: 0;
    top: 128px;
    text-align: center;
  }
  .brand__name {
    font-family: "Tinos", serif;
    font-weight: 400;
    font-size: 50px;
    line-height: 1;
    color: var(--ink);
  }
  .brand__rule {
    width: 300px;
    height: 1px;
    margin: 12px auto 8px;
    background: var(--gold);
  }
  .brand__tagline {
    font-family: "Tinos", serif;
    font-size: 20px;
    letter-spacing: 14px;
    padding-left: 14px;
    color: var(--gold);
  }
  .contact {
    position: absolute;
    top: 345px;
    left: 72px;
    display: flex;
    align-items: center;
    font-family: "Tinos", serif;
    font-size: 22px;
    color: var(--ink);
  }
  .contact__item { display: flex; align-items: center; }
  .contact__item + .contact__item { margin-left: 36px; }
  .contact__icon { width: 18px; height: 24px; margin-right: 8px; }

  /* Back */
  .appointment {
    position: absolute;
    left: 206px;
    top: 52px;
    font-family: "Montserrat", sans-serif;
  }
  .appointment__title {
    font-weight: 600;
    font-size: 23px;
    margin-bottom: 18px;
  }
  .appointment__field {
    display: flex;
    align-items: flex-end;
    width: 440px;
    height: 60px;
    padding-bottom: 14px;
    font-size: 17px;
  }
  .appointment__field:first-of-type { height: 42px; }
  .appointment__line {
    flex: 1;
    margin-left: 4px;
    border-bottom: 1px solid var(--rule);
    transform: translateY(-3px);
  }
  .notice {
    position: absolute;
    left: 51px;
    top: 348px;
    font-family: "Montserrat", sans-serif;
    font-style: italic;
    font-weight: 300;
    font-size: 17.5px;
    color: var(--ink);
    letter-spacing: 0.3px;
  }
  .notice__phone { font-style: normal; font-weight: 600; }
</style>
</head>
<body>

<section class="card card--front" aria-label="Business card front">
  <div class="brand">
    <div class="brand__name">Rosalind Marie</div>
    <div class="brand__rule"></div>
    <div class="brand__tagline">HAIR SALON</div>
  </div>
  <div class="contact">
    <span class="contact__item">
      <svg class="contact__icon" viewBox="0 0 18 24" aria-hidden="true">
        <path d="M9 1C4.6 1 1.5 4.3 1.5 8.4 1.5 14 9 23 9 23s7.5-9 7.5-14.6C16.5 4.3 13.4 1 9 1z" fill="var(--gold)"/>
        <circle cx="9" cy="8.5" r="3" fill="var(--card)"/>
      </svg>
      527 Willowbend lane York, Pa. 17402
    </span>
    <span class="contact__item">
      <svg class="contact__icon" viewBox="0 0 18 24" aria-hidden="true">
        <path d="M4 4l3 -1 2 5-2 1.5c1 2.5 2.5 4.5 4.5 6L13 14l4 3-1 3c-1 1-3 1-5-.5C6 16 3 11 2.5 7 2.3 5.5 3 4.5 4 4z" fill="var(--gold)"/>
      </svg>
      717-464-3082
    </span>
  </div>
</section>

<section class="card card--back" aria-label="Business card back">
  <div class="appointment">
    <div class="appointment__title">Appointment:</div>
    <div class="appointment__field">Date <span class="appointment__line"></span></div>
    <div class="appointment__field">Time <span class="appointment__line"></span></div>
    <div class="appointment__field">Date <span class="appointment__line"></span></div>
    <div class="appointment__field">Time <span class="appointment__line"></span></div>
  </div>
  <p class="notice">If unable to make appointment contact me ASAP - <span class="notice__phone">717-464-3082</span></p>
</section>

</body>
</html>
```